Attractive Flyer for Moving Company

Our Company called "Harborlight Moving Company".
We provide moving service for home and businesses
We need a flyer for a moving company, located in San Diego, CA USA
Flyer size will be 7 x 5 inches, double sided.

Flyer needs to be very attractive and catchy for eye. I want people to keep it even if they dont need our service. I attached a lot of text in separate word file.
Logo, brief and additional pictures are attached.

Target Market(s)

27 years - 55 Years old

Industry/Entity Type

Moving Company

Colors
ec1f27
3176b5
ffffff

Requirements
Must have
• Attached in Word File
Nice to have
• Please be creative in placing a text and selecting a back ground picture.

```html
<!DOCTYPE html>
<html lang="en">
<head>
<meta charset="utf-8">
<title>Harborlight Moving Company – Voucher Flyer</title>
<link href="https://fonts.googleapis.com/css2?family=Arimo:wght@400;700&family=Oswald:wght@300;400;500;600&display=swap" rel="stylesheet">
<style>
  :root {
    --flyer-red: #8f0507;
    --brand-red: #c8141b;
    --deep-blue: #21507f;
    --ribbon-blue: #2f6ea8;
    --ribbon-shade: #163a5e;
    --ink-white: #ffffff;
    --link-blue: #1f4a7a;
    --note-red: #8b0c0c;
  }
  html, body {
    margin: 0;
    padding: 0;
    overflow: hidden;
    background: #ffffff;
  }
  .flyer {
    position: relative;
    width: 1200px;
    height: 857px;
    overflow: hidden;
    background: var(--flyer-red);
    font-family: "Arimo", Arial, sans-serif;
    color: var(--ink-white);
  }
  .backdrop {
    position: absolute;
    inset: 0;
    width: 1200px;
    height: 857px;
  }
  .brand-name {
    position: absolute;
    left: 72px;
    top: 66px;
    width: 340px;
    margin: 0;
    font-weight: 700;
    font-size: 34px;
    line-height: 1.15;
    color: var(--brand-red);
    text-align: center;
  }
  .brand-mark {
    display: inline-block;
    width: 14px;
    height: 14px;
    border-radius: 50%;
    background: var(--brand-red);
    margin-right: 8px;
    vertical-align: 4px;
  }
  .rates {
    position: absolute;
    left: 565px;
    top: 66px;
    margin: 0;
    font-size: 22.5px;
    line-height: 28.5px;
    white-space: nowrap;
  }
  .rate-row {
    display: flex;
  }
  .rate-price {
    width: 83px;
    font-family: "Oswald", sans-serif;
    font-weight: 400;
    font-size: 22px;
  }
  .mover-photo {
    position: absolute;
    left: 318px;
    top: 392px;
    width: 414px;
    height: 410px;
    background: linear-gradient(160deg, #8a7a66 0%, #9fb0a6 40%, #c9cfd3 65%, #5f7ea3 100%);
    opacity: 0.9;
  }
  .savings {
    position: absolute;
    z-index: 2;
    left: 30px;
    top: 226px;
    width: 320px;
    text-align: center;
    font-family: "Oswald", sans-serif;
    white-space: nowrap;
  }
  .savings span {
    display: block;
  }
  .savings-word {
    font-weight: 500;
    font-size: 112px;
    line-height: 116px;
    transform: scaleX(0.7);
  }
  .savings-range {
    margin-top: 4px;
    font-weight: 400;
    font-size: 118px;
    line-height: 120px;
    letter-spacing: -3px;
    transform: scaleX(0.62);
  }
  .savings-tail {
    margin-top: 0;
    font-weight: 400;
    font-size: 70px;
    line-height: 80px;
    letter-spacing: -1px;
    transform: scaleX(0.66);
  }
  .voucher-ribbon {
    position: absolute;
    left: 578px;
    top: 226px;
    width: 520px;
    height: 110px;
  }
  .voucher-text {
    position: absolute;
    left: 600px;
    top: 238px;
    width: 480px;
    text-align: center;
    font-family: "Oswald", sans-serif;
    font-weight: 600;
    white-space: nowrap;
  }
  .voucher-title {
    display: block;
    font-size: 30px;
    line-height: 36px;
    transform: scaleX(0.85);
  }
  .voucher-date {
    display: block;
    font-size: 27px;
    line-height: 36px;
    transform: scaleX(0.85);
  }
  .included {
    position: absolute;
    left: 772px;
    top: 374px;
    width: 400px;
  }
  .included-title {
    margin: 0 0 14px;
    font-weight: 400;
    font-size: 28px;
    letter-spacing: 1.5px;
  }
  .included-list {
    list-style: none;
    margin: 0;
    padding: 0;
    font-size: 22px;
    line-height: 28.5px;
  }
  .included-list li {
    position: relative;
    padding-left: 52px;
    margin-bottom: 14px;
  }
  .included-list li::before {
    content: "-";
    position: absolute;
    left: 12px;
  }
  .site-link {
    position: absolute;
    left: 824px;
    top: 686px;
    font-size: 21px;
    color: var(--link-blue);
  }
  .fine-print {
    position: absolute;
    left: 788px;
    top: 778px;
    width: 284px;
    margin: 0;
    font-size: 17px;
    line-height: 23px;
    color: var(--note-red);
    padding-left: 36px;
  }
  .fine-print-star {
    position: absolute;
    left: 0;
    top: 4px;
    font-size: 24px;
    color: var(--brand-red);
  }
</style>
</head>
<body>
<div class="flyer">
  <svg class="backdrop" viewBox="0 0 1200 857" aria-hidden="true">
    <defs>
      <linearGradient id="floorShade" x1="0" y1="0" x2="0" y2="1">
        <stop offset="0" stop-color="#d9dcdf"/>
        <stop offset="1" stop-color="#f5f6f7"/>
      </linearGradient>
      <linearGradient id="panelShade" x1="0" y1="0" x2="1" y2="1">
        <stop offset="0" stop-color="#d6d9dc"/>
        <stop offset="0.5" stop-color="#f2f3f4"/>
        <stop offset="1" stop-color="#e4e6e8"/>
      </linearGradient>
      <linearGradient id="steelShade" x1="0" y1="0" x2="1" y2="0">
        <stop offset="0" stop-color="#a5aab0"/>
        <stop offset="1" stop-color="#767c83"/>
      </linearGradient>
    </defs>
    <rect x="0" y="680" width="1200" height="177" fill="url(#floorShade)"/>
    <polygon points="0,172 372,172 0,682" fill="var(--deep-blue)"/>
    <polygon points="372,172 548,172 96,857 0,857 0,682" fill="url(#steelShade)"/>
    <polygon points="0,0 488,0 548,172 0,172" fill="url(#panelShade)"/>
  </svg>

  <h1 class="brand-name"><span class="brand-mark"></span>Harborlight<br>Moving Company</h1>

  <div class="rates">
    <div class="rate-row"><span class="rate-price">$235 -</span><span>3 hours of Moving Service with 2 PRO MOVERS</span></div>
    <div class="rate-row"><span class="rate-price">$335 -</span><span>3 hours of Moving Service with 3 PRO MOVERS</span></div>
    <div class="rate-row"><span class="rate-price"></span><span>+ 20% OFF for boxes and packing supplies.</span></div>
  </div>

  <div class="mover-photo" role="img" aria-label="Photo of two movers carrying a blanket-wrapped, plastic-covered piece of furniture"></div>

  <div class="savings">
    <span class="savings-word">SAVE</span>
    <span class="savings-range">15% -25%</span>
    <span class="savings-tail">on your move</span>
  </div>

  <svg class="voucher-ribbon" viewBox="0 0 520 110" aria-hidden="true">
    <polygon points="470,0 520,0 520,44" fill="var(--ribbon-shade)"/>
    <polygon points="50,0 520,0 448,110 0,110" fill="var(--ribbon-blue)"/>
  </svg>
  <div class="voucher-text">
    <span class="voucher-title">KEEP THIS VOUCHER</span>
    <span class="voucher-date">IT IS VALID UNTIL JANUARY 1ST 2019</span>
  </div>

  <section class="included">
    <h2 class="included-title">INCLUDED IN PRICE</h2>
    <ul class="included-list">
      <li>Protection of your furniture with specialized blankets and plasticwrap.</li>
      <li>Dis-assembly and reassembly of your furniture.</li>
      <li>Wardrobe boxes for the duration of moving process.</li>
    </ul>
  </section>

  <div class="site-link">www.harborlightmoving.com</div>

  <p class="fine-print"><span class="fine-print-star">*</span>Special Deal: Cannot be used with any other promotions or coupons</p>
</div>
</body>
</html>
```